Post it Note design

POST-IT NOTE DESIGN (CONTENT)
Size recommended: 4x6 for handwriting space.
Header (Bold):
Lighting Issue Detected on Your Property
Sub-header:
During our routine night inspection, we noted the following item(s):
Checkbox List:
⬜ Building Lights Out
⬜ Pole Lights Out
⬜ Sign Not Illuminated
⬜ Other ________________________
Action Line:
We can provide a quote or dispatch service right away.
Area for notes
Contact Block (Bold & Centered):
Brovane Fixture Inc.
Service@BrovaneFixture.com
www.BrovaneFixture.com
877-514-0862
Industry/Entity Type
Electrical lighting
Colors
Designer to choose colors to be used in the design.
Look and feel
Each slider illustrates characteristics of the customer's brand and the style your logo design should communicate.

```html
<!DOCTYPE html>
<html lang="en">
<head>
<meta charset="utf-8">
<title>Lighting Issue Notice – Brovane Fixture Inc.</title>
<link rel="stylesheet" href="https://fonts.googleapis.com/css2?family=Archivo+Black&family=Inter:wght@400;500;600;700&display=swap">
<style>
  :root {
    --alert-red: #d90026;
    --brand-blue: #0a0acc;
    --paper: #ffffff;
    --frame: #111111;
    --photo-tone-light: #f2f5f7;
    --photo-tone-mid: #e6ebee;
  }
  * { margin: 0; padding: 0; box-sizing: border-box; }
  html, body {
    width: 1200px; height: 1200px; overflow: hidden;
    background: var(--paper);
  }
  body { position: relative; font-family: "Inter", Arial, sans-serif; color: var(--brand-blue); }

  .note {
    position: absolute; left: 197px; top: 72px;
    width: 813px; height: 1062px;
    border: 1px solid var(--frame);
    background: var(--paper);
    overflow: hidden;
  }
  .note__photo {
    position: absolute; left: 10px; top: 478px;
    width: 793px; height: 584px;
    background: radial-gradient(ellipse at 55% 40%, var(--photo-tone-mid) 0%, var(--photo-tone-light) 55%, rgba(255,255,255,0) 80%);
  }
  .note__header {
    position: absolute; left: 0; top: 0; width: 100%; height: 109px;
    background: var(--alert-red);
    color: var(--paper);
    font-family: "Archivo Black", Arial, sans-serif;
    font-size: 42px; line-height: 51px; letter-spacing: 1.5px;
    text-align: center; text-transform: uppercase;
    padding-top: 4px;
  }
  .intro {
    position: absolute; left: 60px; top: 116px; width: 720px;
    font-size: 27px; font-weight: 500; line-height: 35px;
  }
  .checklist { position: absolute; left: 63px; top: 219px; list-style: none; }
  .checklist__item {
    display: flex; align-items: center; height: 50.6px;
    font-size: 28px; font-weight: 500;
  }
  .checklist__box {
    width: 39px; height: 38px; border: 2.5px solid var(--brand-blue);
    border-radius: 6px; margin-right: 24px; flex: none;
  }
  .checklist__blank {
    display: inline-block; width: 350px; margin-left: 8px;
    border-bottom: 2px solid var(--brand-blue); height: 24px;
  }
  .action {
    position: absolute; left: 0; top: 447px; width: 100%;
    text-align: center; font-size: 28px; font-weight: 500;
  }
  .notes-title {
    position: absolute; left: 0; top: 512px; width: 100%;
    text-align: center; font-family: "Archivo Black", Arial, sans-serif;
    font-size: 28px; letter-spacing: 1px;
  }
  .notes-lines { position: absolute; left: 23px; top: 600px; }

  .brand-name {
    position: absolute; left: 72px; top: 903px; width: 265px;
    text-align: center; font-size: 32px; font-weight: 700; line-height: 36px;
  }
  .contact {
    position: absolute; left: 330px; top: 880px; width: 440px;
    text-align: center;
  }
  .contact__name { font-size: 30px; font-weight: 700; line-height: 38px; }
  .contact__line { font-size: 20px; line-height: 26px; }
</style>
</head>
<body>
  <section class="note">
    <div class="note__photo" role="img" aria-label="Faint background photo of a technician servicing parking lot pole light fixtures"></div>

    <h1 class="note__header">Lighting Issue Detected on<br>Your Property</h1>

    <p class="intro">During our routine night inspection, we noted the following item(s):</p>

    <ul class="checklist">
      <li class="checklist__item"><span class="checklist__box"></span>Building Lights Out</li>
      <li class="checklist__item"><span class="checklist__box"></span>Pole Lights Out</li>
      <li class="checklist__item"><span class="checklist__box"></span>Sign Not Illuminated</li>
      <li class="checklist__item"><span class="checklist__box"></span>Other<span class="checklist__blank"></span></li>
    </ul>

    <p class="action">We can provide a quote or dispatch service right away.</p>

    <h2 class="notes-title">TECHNICIAN NOTES &amp; DETAILS</h2>

    <svg class="notes-lines" width="766" height="210" viewBox="0 0 766 210" aria-hidden="true">
      <g stroke="var(--brand-blue)" stroke-width="1.5" stroke-dasharray="12 9">
        <line x1="0" y1="4" x2="766" y2="4"/>
        <line x1="0" y1="45" x2="766" y2="45"/>
        <line x1="0" y1="85" x2="766" y2="85"/>
        <line x1="0" y1="125" x2="766" y2="125"/>
        <line x1="0" y1="165" x2="766" y2="165"/>
        <line x1="0" y1="206" x2="766" y2="206"/>
      </g>
    </svg>

    <p class="brand-name">Brovane<br>Fixture</p>

    <address class="contact" style="font-style:normal">
      <p class="contact__name">Brovane Fixture Inc.</p>
      <p class="contact__line">Service@BrovaneFixture.com</p>
      <p class="contact__line">www.BrovaneFixture.com</p>
      <p class="contact__line">877-514-0862</p>
    </address>
  </section>
</body>
</html>
```